Business Card Design Project

I have just chosen a logo and would now like this designed onto a business card for my hair salon. I would like it to be classy not to busy and have a wow factor when people look at them
Has to Include on card:
Logo Design
And business details below
Kellie-ann Drummond (owner)
0482 736 219
Rdw@vomblet.com.au
71 Willowmere Rise Corvin Cove
Logo is now attached please provide designs
Hair

```html
<!DOCTYPE html>
<html lang="en">
<head>
<meta charset="utf-8">
<title>Redwood Hair Studio – Business Card</title>
<link rel="stylesheet" href="https://fonts.googleapis.com/css2?family=Libre+Baskerville:wght@700&display=swap">
<style>
  :root {
    --card-blue: #2340ff;
    --text-white: #ffffff;
  }
  html, body {
    margin: 0;
    padding: 0;
    overflow: hidden;
  }
  .card {
    position: relative;
    width: 1200px;
    height: 686px;
    background: var(--card-blue);
    overflow: hidden;
    font-family: "Libre Baskerville", "Times New Roman", serif;
    font-weight: 700;
    color: var(--text-white);
  }
  .brand {
    position: absolute;
    left: 25px;
    top: 171px;
    width: 640px;
    height: 335px;
    display: flex;
    flex-direction: column;
    align-items: center;
    justify-content: center;
    text-align: center;
    line-height: 1.15;
    font-size: 64px;
    letter-spacing: 1px;
  }
  .details {
    position: absolute;
    left: 734px;
    top: 252px;
    font-size: 24px;
    line-height: 36px;
    letter-spacing: 0.3px;
  }
  .details p {
    margin: 0;
  }
  .details .contact-group + .contact-group {
    margin-top: 18px;
  }
</style>
</head>
<body>
  <main class="card">
    <div class="brand">
      <span class="brand-name">Redwood<br>Hair Studio</span>
    </div>
    <section class="details">
      <div class="contact-group">
        <p class="owner">Kellie-ann Drummond (owner)</p>
        <p class="phone">0482 736 219</p>
      </div>
      <div class="contact-group">
        <p class="email">Rdw@vomblet.com.au</p>
        <p class="address">71 Willowmere Rise Corvin Cove</p>
      </div>
    </section>
  </main>
</body>
</html>
```